Wellspring Care Alliance Vonzo Ads

We want an ad created for the gay dating app vonzo. The size is 300x250. We want the ad to be sexy, with a shirtless man. We are advertising our free HIV and PrEP services. We are open to slogans about maybe "Bringing HIV and PrEP To You"
"Free PrEP and HIV Management"
Open to ideas.

We also offer through the Harborlight Support Fund
Copay Assistance, Insurance Premium Assistance, Free Medical Services, etc
Our website is wcanj.org

I do want the ad to have a Book Now Button

Gay sexually active males

```html
<!DOCTYPE html>
<html lang="en">
<head>
<meta charset="utf-8">
<title>Wellspring Care Alliance – Vonzo Ad</title>
<link href="https://fonts.googleapis.com/css2?family=Poppins:wght@400;500;600;700&display=swap" rel="stylesheet">
<style>
  :root {
    --page: #e6e6e9;
    --night: #050308;
    --white: #ffffff;
    --ink: #111114;
    --blue: #3d7bff;
    --purple: #8a4dff;
    --pink: #ff4fa3;
    --coral: #ff6f6a;
    --brand: #7a3fe0;
  }
  * { margin: 0; padding: 0; box-sizing: border-box; }
  html, body { width: 1200px; height: 1040px; overflow: hidden; }
  body { background: var(--page); font-family: "Poppins", sans-serif; position: relative; }

  .ad {
    position: absolute; left: 0; top: 20px;
    width: 1200px; height: 1000px; overflow: hidden;
    background: var(--night);
  }
  .ad-backdrop { position: absolute; inset: 0; }

  .headline {
    position: absolute; left: 52px; top: 28px;
    color: var(--white); font-weight: 500;
    font-size: 112px; line-height: 112px; letter-spacing: 1px;
    text-transform: uppercase;
  }
  .headline .accent {
    background: linear-gradient(90deg, var(--blue), var(--purple) 55%, var(--pink));
    -webkit-background-clip: text; background-clip: text; color: transparent;
  }

  .benefits { position: absolute; left: 58px; top: 386px; list-style: none; color: var(--white); }
  .benefits li {
    display: flex; align-items: flex-start; gap: 20px;
    font-size: 38px; line-height: 46px; margin-bottom: 22px;
  }
  .benefits svg { flex: none; width: 32px; height: 32px; margin-top: 8px; }

  .book-button {
    position: absolute; left: 46px; top: 804px;
    width: 474px; height: 80px; border-radius: 40px;
    background: linear-gradient(90deg, var(--blue), var(--purple) 45%, var(--pink) 80%, var(--coral));
    color: var(--white); font-weight: 700; font-size: 46px; letter-spacing: 1px;
    display: flex; align-items: center; justify-content: center;
  }

  .site-link {
    position: absolute; left: 106px; top: 900px;
    font-size: 46px; line-height: 60px; color: var(--ink); font-weight: 400;
  }
  .site-link strong { font-weight: 600; }

  .brand-mark {
    position: absolute; left: 744px; top: 846px;
    display: flex; align-items: center; gap: 22px;
  }
  .brand-dot { width: 84px; height: 84px; border-radius: 50%; background: var(--brand); flex: none; }
  .brand-name { color: var(--brand); font-weight: 600; font-size: 36px; line-height: 44px; }
</style>
</head>
<body>
  <div class="ad">
    <svg class="ad-backdrop" width="1200" height="1000" viewBox="0 0 1200 1000">
      <defs>
        <radialGradient id="glow" cx="0.05" cy="0.02" r="0.75">
          <stop offset="0" stop-color="#3c3aa8"/>
          <stop offset="0.35" stop-color="#4a2470"/>
          <stop offset="0.75" stop-color="#12081c"/>
          <stop offset="1" stop-color="#050308"/>
        </radialGradient>
        <linearGradient id="ring" x1="0" y1="1" x2="1" y2="0">
          <stop offset="0" stop-color="#3d7bff"/>
          <stop offset="0.5" stop-color="#8a4dff"/>
          <stop offset="1" stop-color="#ff4fa3"/>
        </linearGradient>
        <linearGradient id="photoTone" x1="0" y1="0" x2="1" y2="1">
          <stop offset="0" stop-color="#a3a3a3"/>
          <stop offset="0.5" stop-color="#5e5e5e"/>
          <stop offset="1" stop-color="#1c1c1c"/>
        </linearGradient>
      </defs>
      <rect width="1200" height="1000" fill="url(#glow)"/>
      <circle cx="922" cy="472" r="300" fill="none" stroke="url(#ring)" stroke-width="8"/>
      <circle role="img" aria-label="Black and white photo of a shirtless man in light briefs, holding his torso" cx="922" cy="472" r="290" fill="url(#photoTone)"/>
      <path d="M0 1000 V846 H600 C680 846 680 782 760 782 H1200 V1000 Z" fill="#ffffff"/>
    </svg>

    <h1 class="headline">
      Bringing <span class="accent">HIV</span><br>
      And <span class="accent">PrEP</span><br>
      To You
    </h1>

    <ul class="benefits">
      <li><svg viewBox="0 0 32 32"><circle cx="16" cy="16" r="13" fill="none" stroke="#fff" stroke-width="3"/><path d="M9 16 l5 5 l11 -13" fill="none" stroke="#c25cff" stroke-width="4" stroke-linecap="round" stroke-linejoin="round"/></svg>Harborlight Support Fund</li>
      <li><svg viewBox="0 0 32 32"><circle cx="16" cy="16" r="13" fill="none" stroke="#fff" stroke-width="3"/><path d="M9 16 l5 5 l11 -13" fill="none" stroke="#c25cff" stroke-width="4" stroke-linecap="round" stroke-linejoin="round"/></svg>Copay Assistance,</li>
      <li><svg viewBox="0 0 32 32"><circle cx="16" cy="16" r="13" fill="none" stroke="#fff" stroke-width="3"/><path d="M9 16 l5 5 l11 -13" fill="none" stroke="#c25cff" stroke-width="4" stroke-linecap="round" stroke-linejoin="round"/></svg>Insurance Premium<br>Assistance,</li>
      <li><svg viewBox="0 0 32 32"><circle cx="16" cy="16" r="13" fill="none" stroke="#fff" stroke-width="3"/><path d="M9 16 l5 5 l11 -13" fill="none" stroke="#c25cff" stroke-width="4" stroke-linecap="round" stroke-linejoin="round"/></svg>Free Medical Services,</li>
    </ul>

    <div class="book-button">BOOK NOW</div>

    <p class="site-link">www.<strong>wcanj</strong>.org</p>

    <div class="brand-mark">
      <span class="brand-dot"></span>
      <span class="brand-name">Wellspring Care<br>Alliance</span>
    </div>
  </div>
</body>
</html>
```